Brightwell Mechanical - Business Card Design

We would like a dark (likely black) themed business card to be able to hand out to potential clients. We may list our services on the card or keep it clean. Unsure. Logo attached

```html
<!DOCTYPE html>
<html lang="en">
<head>
<meta charset="utf-8">
<title>Brightwell Mechanical – Business Card</title>
<link rel="stylesheet" href="https://fonts.googleapis.com/css2?family=Roboto:wght@400;500;700;900&display=swap">
<style>
  :root {
    --backdrop: #5b5d60;
    --card: #121316;
    --blue: #1f73c2;
    --orange: #f0561d;
    --text-font: "Roboto", Arial, sans-serif;
  }
  * { box-sizing: border-box; margin: 0; padding: 0; }
  html, body { width: 1200px; height: 965px; overflow: hidden; }
  body {
    background: var(--backdrop);
    font-family: var(--text-font);
    display: flex;
    flex-direction: column;
    align-items: center;
    justify-content: center;
    gap: 30px;
  }
  .card {
    position: relative;
    width: 760px;
    height: 434px;
    background: var(--card);
    box-shadow: 0 8px 24px rgba(0,0,0,.35);
    overflow: hidden;
  }

  /* Brand name lockup */
  .brand {
    display: flex;
    align-items: center;
    gap: 12px;
  }
  .brand-dot {
    width: 20px; height: 20px;
    border-radius: 50%;
    background: var(--orange);
    flex: none;
  }
  .brand-name {
    font-weight: 900;
    color: var(--blue);
    text-transform: uppercase;
    line-height: 1.02;
    letter-spacing: .5px;
    white-space: nowrap;
  }

  /* Front side */
  .card-front {
    display: flex;
    flex-direction: column;
    align-items: center;
    padding-top: 92px;
  }
  .card-front .brand-name { font-size: 40px; text-align: left; }
  .services {
    list-style: none;
    margin-top: 30px;
    text-align: center;
  }
  .services li {
    color: var(--blue);
    font-size: 19px;
    line-height: 27px;
  }
  .services li::before,
  .services li::after {
    content: "";
    display: inline-block;
    width: 18px;
    height: 2px;
    background: var(--orange);
    vertical-align: middle;
    margin: 0 9px;
  }

  /* Back side */
  .card-back .brand {
    position: absolute;
    left: 40px;
    top: 200px;
  }
  .card-back .brand-name { font-size: 30px; }
  .divider {
    position: absolute;
    left: 410px;
    top: 95px;
    width: 2px;
    height: 200px;
    background: var(--orange);
  }
  .contact {
    position: absolute;
    left: 440px;
    top: 95px;
  }
  .person-name {
    color: var(--orange);
    font-weight: 700;
    font-size: 28px;
    text-transform: uppercase;
    letter-spacing: .3px;
    white-space: nowrap;
  }
  .person-role {
    color: var(--blue);
    font-size: 19px;
    margin-top: 2px;
  }
  .contact-list {
    list-style: none;
    margin-top: 14px;
  }
  .contact-list li {
    display: flex;
    align-items: center;
    gap: 10px;
    color: var(--blue);
    font-size: 18px;
    line-height: 26px;
    white-space: nowrap;
  }
  .contact-list svg { width: 16px; height: 16px; flex: none; }
  .address {
    color: var(--blue);
    font-size: 18px;
    line-height: 25px;
    font-style: normal;
    margin-top: 16px;
    padding-left: 26px;
    white-space: nowrap;
  }
  .stripe {
    position: absolute;
    left: 0; right: 0; bottom: 0;
    height: 12px;
    display: flex;
  }
  .stripe-orange { flex: 1; background: var(--orange); }
  .stripe-blue { flex: 1; background: var(--blue); }
</style>
</head>
<body>

  <section class="card card-front">
    <div class="brand">
      <span class="brand-dot"></span>
      <span class="brand-name">Brightwell<br>Mechanical Inc</span>
    </div>
    <ul class="services">
      <li>Plumbing Service and Maintenance</li>
      <li>HVAC and Air Conditioning Installations and Maintenance</li>
      <li>Sanitary Flushing and Drain Cleaning</li>
      <li>Boiler Servicing</li>
      <li>Backflow Testing</li>
      <li>Gas Fitting</li>
    </ul>
  </section>

  <section class="card card-back">
    <div class="brand">
      <span class="brand-dot"></span>
      <span class="brand-name">Brightwell<br>Mechanical Inc</span>
    </div>
    <div class="divider"></div>
    <div class="contact">
      <h1 class="person-name">Daniel Ostrander</h1>
      <p class="person-role">Director/ CEO</p>
      <ul class="contact-list">
        <li>
          <svg viewBox="0 0 16 16" aria-hidden="true"><path d="M4 1.5 6 4.5 4.8 6c.8 2 2.4 3.6 4.4 4.4L10.7 9.2l3 2-1.2 2.6C7 13.5 2.5 9 2.2 3.6Z" fill="none" stroke="#f0561d" stroke-width="1.4" stroke-linejoin="round"/></svg>
          +1 555-014-2290
        </li>
        <li>
          <svg viewBox="0 0 16 16" aria-hidden="true"><rect x="1.5" y="3.5" width="13" height="9" fill="none" stroke="#f0561d" stroke-width="1.4"/><path d="M1.5 3.5 8 9l6.5-5.5" fill="none" stroke="#f0561d" stroke-width="1.4"/></svg>
          info@brightwellmechanical.com
        </li>
      </ul>
      <address class="address">4-2150 Harlow Ave SE, Fairmont<br>AB T0X 1K2, Canada</address>
    </div>
    <div class="stripe">
      <span class="stripe-orange"></span>
      <span class="stripe-blue"></span>
    </div>
  </section>

</body>
</html>
```